Graduates Circle Sponsorship Brochure

The University of Glenmarrow Alumni Club of New York is putting together a brochure to solicit corporate sponsors for our 5th annual black tie gala in downtown Manhattan.
The Graduates Circle works to benefit both the alumni community and to give back to the University. Our Lantern Dance seeks to bring together former students, friends, and family of Glenmarrow to remind them of their own Lantern Dance experience during university. We are also promoting Scottish-American relations, and want to make clear to sponsors the benefit of access to our demographic.

Target Market(s)

Corporations, Special Interest Groups, parties with affiliation to Scotland and the UK.

Industry/Entity Type

Non-Profit

Font styles to use
Serif

Colors
ec1f27
0255a3

Requirements
Must have
• Clear details about the separation of sponsorship price points, emphasis on the potential impact and benefit of partnership.
Nice to have
• Some big pictures and lots of icons to show the different sponsorship levels.

```html
<!DOCTYPE html>
<html lang="en">
<head>
<meta charset="utf-8">
<title>Lantern Dance 2018 – Sponsorship Brochure</title>
<link rel="stylesheet" href="https://fonts.googleapis.com/css2?family=Cinzel:wght@400;700;900&family=Open+Sans:wght@400;600;700&display=swap">
<style>
  :root {
    --stage: #d9d6d1;
    --page: #121212;
    --page-2: #1e1e1e;
    --gold: #e3a72f;
    --gold-light: #f7d77a;
    --gold-dark: #9a6a14;
    --silver: #c9c9c9;
    --silver-dark: #6e6e6e;
    --bronze: #c9875a;
    --bronze-dark: #7c4a2a;
    --red: #ec1f27;
    --blue: #0255a3;
    --body: #d8d8d8;
    --muted: #a7a7a7;
    --rule: #3a3a3a;
  }
  * { box-sizing: border-box; margin: 0; padding: 0; }
  html, body { width: 1200px; height: 675px; overflow: hidden; }
  body { background: var(--stage); font-family: "Open Sans", Arial, sans-serif; }

  .canvas { position: relative; width: 1200px; height: 675px; }
  .page {
    position: absolute; top: 28px; width: 480px; height: 620px;
    background: linear-gradient(180deg, var(--page-2), var(--page));
    box-shadow: 0 6px 18px rgba(0,0,0,.35);
    overflow: hidden; color: var(--body);
  }
  .page--front { left: 100px; }
  .page--back { left: 620px; }

  /* ---------- front page ---------- */
  .club-mark {
    position: absolute; top: 22px; left: 0; right: 0;
    display: flex; justify-content: center; align-items: center; gap: 6px;
    font-family: "Cinzel", Georgia, serif; font-size: 10px; font-weight: 700;
    color: var(--gold); letter-spacing: 1px;
  }
  .club-mark__dot { width: 14px; height: 14px; border-radius: 50%; background: var(--gold); }
  .ornament {
    position: absolute; left: 110px; right: 110px; height: 14px;
    background: linear-gradient(90deg, transparent, var(--gold-dark), var(--gold-light), var(--gold-dark), transparent);
    opacity: .7; border-radius: 7px;
  }
  .ornament--top { top: 44px; }
  .ornament--bottom { top: 168px; }
  .event-title {
    position: absolute; top: 62px; left: 0; right: 0; text-align: center;
    font-family: "Cinzel", Georgia, serif; font-weight: 900; line-height: 1;
    background: linear-gradient(180deg, var(--gold-light), var(--gold) 55%, var(--gold-dark));
    -webkit-background-clip: text; background-clip: text; color: transparent;
  }
  .event-title__name { display: block; font-size: 44px; letter-spacing: 1px; }
  .event-title__year { display: block; font-size: 38px; margin-top: 6px; }
  .title-band {
    position: absolute; top: 196px; left: 0; right: 0; height: 38px;
    background: linear-gradient(90deg, var(--gold-dark), var(--gold) 30%, var(--gold-light) 55%, var(--gold) 80%, var(--gold-dark));
    display: flex; align-items: center; justify-content: center;
    font-family: "Cinzel", Georgia, serif; font-size: 24px; letter-spacing: 2px; color: #fff6dc;
    text-shadow: 0 1px 2px rgba(0,0,0,.35);
  }
  .intro {
    position: absolute; top: 250px; left: 24px; right: 24px;
    font-size: 7.3px; line-height: 1.5; text-align: justify;
  }
  .tier-ribbon {
    position: absolute; left: 0; width: 140px; padding: 6px 0 6px 16px;
    font-family: "Cinzel", Georgia, serif; font-weight: 700; color: #fff; line-height: 1;
  }
  .tier-ribbon__name { display: block; font-size: 15px; }
  .tier-ribbon__price { display: block; font-size: 12px; margin-top: 4px; font-family: "Open Sans", Arial, sans-serif; }
  .tier-ribbon--gold {
    top: 358px; width: 150px;
    background: linear-gradient(90deg, var(--gold-dark), var(--gold) 60%, var(--gold-light));
  }
  .tier-text {
    position: absolute; font-size: 7.3px; line-height: 1.5;
  }
  .tier-text p + p, .tier-text p + ul { margin-top: 5px; }
  .tier-text ul { padding-left: 10px; }
  .tier-text li { margin-top: 2px; }
  .tier-text--gold { top: 352px; left: 170px; right: 22px; }
  .gold-stars { position: absolute; top: 420px; left: 30px; }
  .footer-band {
    position: absolute; bottom: 12px; left: 0; right: 0; height: 12px;
    background: linear-gradient(90deg, var(--gold-dark), var(--gold), var(--gold-dark));
  }

  /* ---------- back page ---------- */
  .tier-ribbon--silver { top: 24px; background: linear-gradient(90deg, var(--silver-dark), var(--silver) 70%, #efefef); color: #222; }
  .tier-ribbon--bronze { top: 168px; background: linear-gradient(90deg, var(--bronze-dark), var(--bronze) 70%, #e6ad84); }
  .tier-ribbon--support { top: 318px; width: 150px; padding: 0; }
  .support-name { background: var(--red); padding: 5px 0 5px 14px; font-size: 13px; line-height: 1.05; }
  .support-price { background: var(--blue); padding: 4px 0 4px 14px; font-size: 12px; font-family: "Open Sans", Arial, sans-serif; text-align: center; }
  .tier-text--silver { top: 20px; left: 166px; right: 22px; }
  .tier-text--bronze { top: 162px; left: 166px; right: 22px; }
  .tier-text--support { top: 318px; left: 166px; right: 22px; }
  .silver-stars { position: absolute; top: 84px; left: 18px; }
  .bronze-stars { position: absolute; top: 226px; left: 30px; }
  .divider { position: absolute; left: 0; right: 0; height: 1px; background: var(--rule); }
  .divider--one { top: 148px; }
  .divider--two { top: 300px; }
  .club-info {
    position: absolute; top: 376px; left: 0; right: 0; bottom: 0;
    background: linear-gradient(180deg, #1b1b1b, #262626);
    padding: 22px 24px 0;
    font-size: 7.3px; line-height: 1.5; text-align: justify;
  }
  .club-info p + p { margin-top: 7px; }
  .address {
    margin-top: 14px; text-align: center; color: var(--muted);
    font-weight: 700; font-size: 11px; line-height: 1.3;
  }
</style>
</head>
<body>
<main class="canvas">

  <!-- Front page -->
  <section class="page page--front">
    <div class="club-mark"><span class="club-mark__dot"></span>Graduates Circle</div>
    <div class="ornament ornament--top" role="img" aria-label="Gold scroll ornament above the title"></div>
    <h1 class="event-title">
      <span class="event-title__name">LANTERN DANCE</span>
      <span class="event-title__year">2018</span>
    </h1>
    <div class="ornament ornament--bottom" role="img" aria-label="Gold scroll ornament below the title"></div>
    <div class="title-band">SPONSORSHIP BROCHURE</div>

    <p class="intro">The University of Glenmarrow Alumni Club of New York, a registered 501(c)3 charity, invites you to participate in our 5th annual Lantern Dance. Since its inception, the Lantern Dance has been a means to foster the community of alumni, parents and friends of the University of Glenmarrow and other Scottish universities in the greater New York area. All sponsors will have the opportunity to showcase their products to a select audience, and every sponsor will be listed in our ball brochure, which is handed out to each guest as they arrive. Additional sponsorship levels feature treatment and placement of logos or other advertisement within the brochure.</p>

    <div class="tier-ribbon tier-ribbon--gold">
      <span class="tier-ribbon__name">GOLD<br>SPONSOR</span>
      <span class="tier-ribbon__price">$10,000</span>
    </div>
    <svg class="gold-stars" width="100" height="96" viewBox="0 0 100 96" aria-hidden="true">
      <defs>
        <linearGradient id="goldStar" x1="0" y1="0" x2="1" y2="1">
          <stop offset="0" stop-color="#f7d77a"/><stop offset=".55" stop-color="#e3a72f"/><stop offset="1" stop-color="#9a6a14"/>
        </linearGradient>
      </defs>
      <polygon fill="url(#goldStar)" points="50,2 62,36 98,36 69,58 80,94 50,72 20,94 31,58 2,36 38,36"/>
    </svg>
    <div class="tier-text tier-text--gold">
      <p>As the premier sponsor behind this prestigious event, the Gold Sponsor will be the driving force behind the black-tie gala dinner.</p>
      <p>The Gold Sponsor will receive the following benefits:</p>
      <ul>
        <li>Billed as the event sponsor, appearing alongside the Graduates Circle of New York.</li>
        <li>Prominent display on the event invitation, tickets, the front page of the brochure and any other printed or electronic materials.</li>
        <li>Special recognition from our keynote speaker during the banquet.</li>
        <li>3 Complimentary Tickets</li>
      </ul>
    </div>
    <div class="footer-band"></div>
  </section>

  <!-- Back page -->
  <section class="page page--back">
    <div class="tier-ribbon tier-ribbon--silver">
      <span class="tier-ribbon__name">SILVER<br>SPONSOR</span>
      <span class="tier-ribbon__price">$5,000</span>
    </div>
    <svg class="silver-stars" width="120" height="46" viewBox="0 0 120 46" aria-hidden="true">
      <defs>
        <linearGradient id="silverStar" x1="0" y1="0" x2="1" y2="1">
          <stop offset="0" stop-color="#ffffff"/><stop offset=".6" stop-color="#c9c9c9"/><stop offset="1" stop-color="#6e6e6e"/>
        </linearGradient>
      </defs>
      <polygon fill="url(#silverStar)" points="24,1 30,17 47,17 33,27 38,44 24,34 10,44 15,27 1,17 18,17"/>
      <polygon fill="url(#silverStar)" points="84,1 90,17 107,17 93,27 98,44 84,34 70,44 75,27 61,17 78,17"/>
    </svg>
    <div class="tier-text tier-text--silver">
      <p>Our two silver sponsors will help to support the live entertainment and featured cocktail hour.</p>
      <p>Each Silver Sponsor will receive the following benefits:</p>
      <ul>
        <li>Prominent display in their respective sponsored area, banners, table decorations and other signage.</li>
        <li>Recognition from our keynote speaker during the banquet.</li>
        <li>Special acknowledgement in the brochure, on the website and on our social media pages.</li>
        <li>2 Complimentary Tickets</li>
      </ul>
    </div>
    <div class="divider divider--one"></div>

    <div class="tier-ribbon tier-ribbon--bronze">
      <span class="tier-ribbon__name">BRONZE<br>SPONSOR</span>
      <span class="tier-ribbon__price">$3,000</span>
    </div>
    <svg class="bronze-stars" width="90" height="66" viewBox="0 0 90 66" aria-hidden="true">
      <defs>
        <linearGradient id="bronzeStar" x1="0" y1="0" x2="1" y2="1">
          <stop offset="0" stop-color="#f0c08a"/><stop offset=".6" stop-color="#c9875a"/><stop offset="1" stop-color="#7c4a2a"/>
        </linearGradient>
      </defs>
      <polygon fill="url(#bronzeStar)" points="18,2 22,13 34,13 24,20 28,32 18,25 8,32 12,20 2,13 14,13"/>
      <polygon fill="url(#bronzeStar)" points="68,0 72,11 84,11 74,18 78,30 68,23 58,30 62,18 52,11 64,11"/>
      <polygon fill="url(#bronzeStar)" points="46,32 50,43 62,43 52,50 56,62 46,55 36,62 40,50 30,43 42,43"/>
    </svg>
    <div class="tier-text tier-text--bronze">
      <p>Our three bronze sponsors will help to support our signature cocktail rooms, located in the library, the bar and the piano room.</p>
      <p>Each Bronze Sponsor will receive the following benefits:</p>
      <ul>
        <li>Prominent display in their respective cocktail room through banners, table decorations and other signage.</li>
        <li>Special acknowledgement in the brochure and on the website.</li>
        <li>1 Complimentary Ticket to the Gala</li>
      </ul>
    </div>
    <div class="divider divider--two"></div>

    <div class="tier-ribbon tier-ribbon--support">
      <div class="support-name">SUPPORTING<br>SPONSOR</div>
      <div class="support-price">$750</div>
    </div>
    <div class="tier-text tier-text--support">
      <p>Our Supporting Sponsors form the pillars of our community.</p>
    </div>

    <div class="club-info">
      <p>The University of Glenmarrow Alumni Club of New York has a long history of fostering a sense of community in the New York area. We provide opportunities for alumni, current students, parents and friends to meet, network and socialise. We hold a number of events during the year, including an Opening Reception, a Burns Night, a Tartan Day Parade, and a Summer Party. We also support any events or guests from the University who are visiting the New York area.</p>
      <p>The University of Glenmarrow Alumni Club of New York is a registered 501(c)3 public charity. As such, the Graduates Circle is seeking financial support in order to be able to host quality events, and other projects that support the University, such as the construction of new conference rooms in the Students' Union.</p>
      <p>If you are interested in making a donation, please send a check payable to the University of Glenmarrow Graduates Circle of New York to the following address:</p>
      <address class="address">
        University of Glenmarrow<br>
        Graduates Circle of New York<br>
        48 Harbor Lane / Suite 902 / New York, NY
      </address>
    </div>
  </section>

</main>
</body>
</html>
```